Dr. Pell Works
Business card, stationary, fax page, envelope
Dr. Pell Works - Corporate Services
Creative Brief
Bright & Fun-filled
Grant Bevis Hallworth
Senior Account Executive
417 S. Tavish Ave Los Angeles CA 90012
grant@drpellworks.example
drpellworks.example
I also have 4 other people that need their won business cards but with their cell phone and title info.

```html
<!DOCTYPE html>
<html lang="en">
<head>
<meta charset="utf-8">
<title>Dr. Pell Works — Stationery Set</title>
<link href="https://fonts.googleapis.com/css2?family=Fredoka:wght@600&family=Roboto:wght@400;700&display=swap" rel="stylesheet">
<style>
  :root{
    --paper:#ffffff;
    --peach:#f9b58f;
    --peach-light:#fcd3bb;
    --orange:#f28a4e;
    --yellow:#fdc600;
    --ink:#1a1a1a;
    --grey:#6b6b6b;
    --line:#c9c9c9;
    --shadow:0 1px 4px rgba(0,0,0,.28);
  }
  *{margin:0;padding:0;box-sizing:border-box}
  html,body{width:1200px;height:463px;overflow:hidden;background:#fff}
  .stage{position:relative;width:1200px;height:463px;font-family:"Roboto",Arial,sans-serif;color:var(--ink)}
  .piece{position:absolute;background:var(--paper);box-shadow:var(--shadow);overflow:hidden}
  .piece > svg.band{position:absolute;left:0;top:0;width:100%;height:100%}
  .brand{position:absolute;display:flex;align-items:center;gap:4px;font-family:"Fredoka",sans-serif;font-weight:600;color:var(--ink);white-space:nowrap;line-height:1}
  .brand .dot{border-radius:50%;background:var(--paper);border:1.5px solid var(--ink);flex:none}
  .brand.on-dark{color:#fff}
  .brand.on-dark .dot{border-color:#fff}
  .tiny{position:absolute;font-size:4px;line-height:5.5px;color:var(--grey);white-space:nowrap}
  .tiny b{color:var(--ink)}

  /* business cards */
  .card-front{left:67px;top:91px;width:101px;height:58px}
  .card-black{left:72px;top:163px;width:84px;height:48px;background:var(--ink)}
  .card-peach{left:158px;top:163px;width:82px;height:48px;background:var(--peach)}

  /* envelopes */
  .env-white{left:48px;top:228px;width:264px;height:163px}
  .env-black{left:888px;top:72px;width:259px;height:161px}
  .env-yellow{left:874px;top:240px;width:266px;height:173px}

  /* sheets */
  .letterhead{left:336px;top:48px;width:197px;height:367px}
  .fax{left:590px;top:48px;width:202px;height:367px}

  .fax-title{position:absolute;right:14px;top:86px;font-size:5px;font-weight:700}
  .fax-table{position:absolute;left:16px;top:94px;width:172px;border-collapse:collapse;font-size:3.6px}
  .fax-table td{border:.6px solid var(--line);height:8px;padding:0 2px;color:var(--grey)}
  .fax-table td.label{width:18px;background:#f3f3f3}
  .fax-checks{position:absolute;left:16px;top:138px;display:flex;gap:8px;font-size:3.6px;color:var(--grey)}
  .fax-checks span::before{content:"";display:inline-block;width:3px;height:3px;border:.5px solid var(--grey);margin-right:1.5px;vertical-align:middle}
  .fax-rule{position:absolute;left:16px;right:14px;top:146px;border-top:.6px solid var(--line)}
</style>
</head>
<body>
<div class="stage">

  <!-- Business card front -->
  <div class="piece card-front">
    <svg class="band" viewBox="0 0 100 58" preserveAspectRatio="none" aria-hidden="true">
      <path d="M0 0H100V14C70 10 35 22 0 30Z" fill="var(--peach)"/>
      <path d="M0 30C35 22 70 10 100 14V16C70 13 35 25 0 33Z" fill="var(--orange)"/>
    </svg>
    <div class="brand" style="left:6px;top:8px;font-size:9px"><span class="dot" style="width:11px;height:11px"></span>Dr. Pell Works</div>
    <div class="tiny" style="left:36px;top:31px;font-size:3.6px;line-height:4.6px"><b>Grant Bevis Hallworth</b><br>Senior Account Executive<br>grant@drpellworks.example</div>
  </div>

  <!-- Business card black -->
  <div class="piece card-black">
    <div class="brand on-dark" style="left:10px;top:18px;font-size:9px"><span class="dot" style="width:11px;height:11px;background:var(--ink)"></span>Dr. Pell Works</div>
  </div>

  <!-- Business card peach -->
  <div class="piece card-peach">
    <svg class="band" viewBox="0 0 82 48" preserveAspectRatio="none" aria-hidden="true">
      <path d="M0 48V36C30 30 55 30 82 36V48Z" fill="var(--paper)"/>
    </svg>
    <div class="tiny" style="left:8px;top:14px;color:var(--ink)">417 S. Tavish Ave<br>Los Angeles CA 90012</div>
  </div>

  <!-- White envelope -->
  <div class="piece env-white">
    <svg class="band" viewBox="0 0 264 163" preserveAspectRatio="none" aria-hidden="true">
      <path d="M0 0H264V62C180 40 90 54 0 88Z" fill="var(--peach)"/>
      <path d="M0 88C90 54 180 40 264 62V66C180 45 90 59 0 93Z" fill="var(--orange)"/>
    </svg>
    <div class="brand" style="left:98px;top:10px;font-size:12px"><span class="dot" style="width:14px;height:14px"></span>Dr. Pell Works</div>
    <div class="tiny" style="left:12px;top:150px">417 S. Tavish Ave Los Angeles CA 90012 &nbsp; drpellworks.example</div>
  </div>

  <!-- Letterhead -->
  <div class="piece letterhead">
    <svg class="band" viewBox="0 0 197 367" preserveAspectRatio="none" aria-hidden="true">
      <path d="M0 0H197V30C130 22 60 40 0 66Z" fill="var(--peach)"/>
      <path d="M0 66C60 40 130 22 197 30V33C130 26 60 44 0 70Z" fill="var(--orange)"/>
    </svg>
    <div class="brand" style="left:10px;top:16px;font-size:11px"><span class="dot" style="width:13px;height:13px"></span>Dr. Pell Works</div>
    <div class="tiny" style="left:10px;top:336px"><b>Phone</b> (213) 555-0148<br><b>Fax</b> (213) 555-0149<br><b>Email</b> grant@drpellworks.example<br><b>Web</b> drpellworks.example</div>
  </div>

  <!-- Fax page -->
  <div class="piece fax">
    <svg class="band" viewBox="0 0 202 367" preserveAspectRatio="none" aria-hidden="true">
      <path d="M0 0H202V30C135 22 62 40 0 66Z" fill="var(--peach)"/>
      <path d="M0 66C62 40 135 22 202 30V33C135 26 62 44 0 70Z" fill="var(--orange)"/>
    </svg>
    <div class="brand" style="left:10px;top:16px;font-size:11px"><span class="dot" style="width:13px;height:13px"></span>Dr. Pell Works</div>
    <div class="fax-title">Fax</div>
    <table class="fax-table">
      <tr><td class="label">To</td><td></td><td class="label">From</td><td></td></tr>
      <tr><td class="label">Fax</td><td></td><td class="label">Pages</td><td></td></tr>
      <tr><td class="label">Phone</td><td></td><td class="label">Date</td><td></td></tr>
      <tr><td class="label">Re</td><td></td><td class="label">CC</td><td></td></tr>
    </table>
    <div class="fax-checks"><span>Urgent</span><span>For Review</span><span>Please Comment</span><span>Please Reply</span></div>
    <div class="fax-rule"></div>
  </div>

  <!-- Black envelope -->
  <div class="piece env-black">
    <svg class="band" viewBox="0 0 259 161" preserveAspectRatio="none" aria-hidden="true">
      <path d="M0 0H259V112C170 70 80 70 0 100Z" fill="var(--ink)"/>
    </svg>
    <div class="brand on-dark" style="left:72px;top:58px;font-size:12px"><span class="dot" style="width:14px;height:14px;background:var(--ink)"></span>Dr. Pell Works</div>
  </div>

  <!-- Yellow envelope -->
  <div class="piece env-yellow">
    <svg class="band" viewBox="0 0 266 173" preserveAspectRatio="none" aria-hidden="true">
      <path d="M0 0H266V70C180 44 90 58 0 92Z" fill="var(--yellow)"/>
      <path d="M0 92C90 58 180 44 266 70V74C180 49 90 63 0 97Z" fill="var(--orange)"/>
    </svg>
    <div class="brand" style="left:102px;top:38px;font-size:12px"><span class="dot" style="width:14px;height:14px"></span>Dr. Pell Works</div>
    <div class="tiny" style="left:12px;top:160px">417 S. Tavish Ave Los Angeles CA 90012</div>
  </div>

</div>
</body>
</html>
```